Party Decoration Set Designs - Rose Gold theme - more example images just added

We are looking for a set of designs for a set of party decorations. It’s a Rose Gold colored theme. I have attached some photos of some glittery rose gold items that I think would go good with the theme. There are also some photos of full sets of decorations in other colors schemes to give an idea of what we are looking for.

We would like to have designs for the items below:

1- Happy Birthday Flag Banner- looking for something unique. Size- 5”X7” WXL

2- hanging swirl cards ( photo examples attached) 4”X6” approx. can be different sizes and shapes.

3- centerpiece designs- photo examples attached. Middle
Piece that’s says Happy Birthday should be 5”X 7” and the smaller surrounding pieces 3X5

4 - round candy stickers and candy wrappers. Examples below. .75 inch

The photos below are of products currently sold. We would like to be very similar to these but just a little different to make our own. And then to have a Happy Birthday banner created to match the theme.

Some of these example photos below are from different themes and colors But I included them because they are the complete set we want to create. First we will do a generic “Happy Birthday” Set with rose gold glitter theme and then later we will add the Sweet 16 birthday theme as well and 40th, 50th etc.

On the centerpieces where the example photos how a large “40”, we would like this to be a larger “Happy Birthday” design. Then surrounded by some smaller designs.
I look forward to receiving your ideas

Target Market(s)

Anyone looking for birthday Peru decorations for a female.

Font styles to use
Other font styles liked:
• Open to designer suggestion

Requirements
Must have
• Happy Birthday Banner, Hanging swirl cards, centerpiece cards, cake topper
Nice to have
• We are certainly open to any creative ideas.
Should not have
• I just now added some example images of a very good set of exactly what we want but its in a different theme. This is a black gold set and our requested design is more feminine and Rose Gold color

```html
<!DOCTYPE html>
<html lang="en">
<head>
<meta charset="utf-8">
<title>Happy Birthday Flag Banner – Rose Gold</title>
<link rel="stylesheet" href="https://fonts.googleapis.com/css2?family=Playfair+Display:wght@700&family=Great+Vibes&family=Cormorant+Garamond:wght@500&display=swap">
<style>
  :root {
    --page: #ffffff;
    --flag-rose: #eea89f;
    --letter: #ffffff;
    --tail-light: #f6d9d2;
    --tail-mid: #e9b3ab;
    --edge-light: #f3d4c8;
    --edge-dark: #cf9d98;
    --art-tone: #f8e3de;
  }
  html, body {
    margin: 0;
    width: 1200px;
    height: 1130px;
    overflow: hidden;
    background: var(--page);
  }
  .banner-sheet { display: block; width: 1200px; height: 1130px; }
  .flag-body { fill: var(--flag-rose); }
  .flag-tail { fill: url(#tailFill); }
  .flag-edge { fill: none; stroke: url(#edgeFill); stroke-width: 7; stroke-linejoin: miter; }
  .flag-letter {
    font-family: "Playfair Display", Georgia, serif;
    font-weight: 700;
    font-size: 204px;
    fill: var(--letter);
    text-anchor: middle;
  }
  .title-caps {
    font-family: "Cormorant Garamond", Georgia, serif;
    font-weight: 500;
    font-size: 38px;
    fill: var(--letter);
    text-anchor: middle;
  }
  .title-script {
    font-family: "Great Vibes", cursive;
    font-size: 58px;
    fill: var(--letter);
    text-anchor: middle;
  }
  .art-slot { fill: var(--art-tone); opacity: 0.85; }
</style>
</head>
<body>
<svg class="banner-sheet" viewBox="0 0 1200 1130" xmlns="http://www.w3.org/2000/svg">
  <defs>
    <linearGradient id="tailFill" x1="0" y1="0" x2="1" y2="0">
      <stop offset="0" stop-color="var(--tail-light)"/>
      <stop offset="0.5" stop-color="var(--tail-mid)"/>
      <stop offset="1" stop-color="var(--tail-light)"/>
    </linearGradient>
    <linearGradient id="edgeFill" x1="0" y1="0" x2="1" y2="0">
      <stop offset="0" stop-color="var(--edge-light)"/>
      <stop offset="0.5" stop-color="var(--edge-dark)"/>
      <stop offset="1" stop-color="var(--edge-light)"/>
    </linearGradient>

    <g id="letterFlag">
      <polygon class="flag-tail" points="0,210 207,210 103.5,290"/>
      <polyline class="flag-edge" points="2,212 103.5,286 205,212"/>
      <rect class="flag-body" x="0" y="0" width="207" height="210"/>
    </g>

    <g id="titleFlag">
      <polygon class="flag-body" points="0,0 207,0 207,210 103.5,290 0,210"/>
      <polyline class="flag-edge" points="2,212 103.5,286 205,212"/>
      <rect class="art-slot" x="55" y="44" width="97" height="10" rx="3" role="img" aria-label="Small leafy flourish ornament"/>
      <text class="title-caps" x="103.5" y="98">HAPPY</text>
      <text class="title-script" x="103.5" y="155">Birthday</text>
      <rect class="art-slot" x="78" y="180" width="50" height="52" rx="4" role="img" aria-label="Tiered birthday cake illustration with candles"/>
    </g>
  </defs>

  <!-- Row 1: HAPPY -->
  <g class="flag-row">
    <g transform="translate(4,0)"><use href="#letterFlag"/><text class="flag-letter" x="103.5" y="187">H</text></g>
    <g transform="translate(239,0)"><use href="#letterFlag"/><text class="flag-letter" x="103.5" y="187">A</text></g>
    <g transform="translate(474,0)"><use href="#letterFlag"/><text class="flag-letter" x="103.5" y="187">P</text></g>
    <g transform="translate(709,0)"><use href="#letterFlag"/><text class="flag-letter" x="103.5" y="187">P</text></g>
    <g transform="translate(943,0)"><use href="#letterFlag"/><text class="flag-letter" x="103.5" y="187">Y</text></g>
  </g>

  <!-- Row 2: BIRTH -->
  <g class="flag-row">
    <g transform="translate(4,326)"><use href="#letterFlag"/><text class="flag-letter" x="103.5" y="187">B</text></g>
    <g transform="translate(239,326)"><use href="#letterFlag"/><text class="flag-letter" x="103.5" y="187">I</text></g>
    <g transform="translate(474,326)"><use href="#letterFlag"/><text class="flag-letter" x="103.5" y="187">R</text></g>
    <g transform="translate(709,326)"><use href="#letterFlag"/><text class="flag-letter" x="103.5" y="187">T</text></g>
    <g transform="translate(943,326)"><use href="#letterFlag"/><text class="flag-letter" x="103.5" y="187">H</text></g>
  </g>

  <!-- Row 3: title flag, DAY, title flag -->
  <g class="flag-row">
    <g transform="translate(4,659)"><use href="#titleFlag"/></g>
    <g transform="translate(239,659)"><use href="#letterFlag"/><text class="flag-letter" x="103.5" y="183">D</text></g>
    <g transform="translate(474,659)"><use href="#letterFlag"/><text class="flag-letter" x="103.5" y="183">A</text></g>
    <g transform="translate(709,659)"><use href="#letterFlag"/><text class="flag-letter" x="103.5" y="183">Y</text></g>
    <g transform="translate(941,659)"><use href="#titleFlag"/></g>
  </g>
</svg>
</body>
</html>
```